KWB needs a professional PP

We are looking for a more professional powerpoint presentation that will be presented to prospective clients. This powerpoint needs to summarize all the services and value that The Harbinger Collective has to offer, pretty much giving an overview of the company.

The clients we deal with are Funeral Homes and Funeral Directors, we are an organization dedicated to assisting funeral homes in implementing highly profitable insurance programs while providing the training, support and service along the way. More information is provided in the brochure attached.

We are going for a professional simple theme, we want to get the message across without overwhelming the client.

I have attached our current powerpoint presentation as reference and more information about the our company and what we offer. This one is obviously what we are looking to replace, but the information will be generally the same. It needs to be more visually appealing and convey professionalism.

```html
<!DOCTYPE html>
<html lang="en">
<head>
<meta charset="utf-8">
<title>The Harbinger Collective – Slide Template</title>
<link href="https://fonts.googleapis.com/css2?family=Cinzel:wght@400;700&family=Open+Sans:wght@400;700&display=swap" rel="stylesheet">
<style>
  :root {
    --brand-blue: #2f66a8;
    --title-grey: #8d9398;
    --body-text: #4a4a4a;
    --header-top: #f3f4f5;
    --header-bottom: #ffffff;
    --rule-grey: #d6d8da;
    --footer-rule: #b9bcc0;
    --footer-blue: #2f6aac;
    --white: #ffffff;
  }
  * { margin: 0; padding: 0; box-sizing: border-box; }
  html, body {
    width: 1200px;
    height: 900px;
    overflow: hidden;
    background: var(--white);
  }
  .slide {
    position: relative;
    width: 1200px;
    height: 900px;
    background: var(--white);
    font-family: "Open Sans", Arial, sans-serif;
  }
  .slide-header {
    position: absolute;
    top: 0; left: 0;
    width: 100%;
    height: 120px;
    background: linear-gradient(var(--header-top), var(--header-bottom));
    border-bottom: 1px solid var(--rule-grey);
  }
  .project-title {
    position: absolute;
    left: 45px;
    top: 32px;
    font-family: "Cinzel", "Times New Roman", serif;
    font-weight: 700;
    font-size: 38px;
    letter-spacing: 2px;
    color: var(--title-grey);
  }
  .project-title .accent { color: var(--brand-blue); }
  .brand-name {
    position: absolute;
    right: 38px;
    top: 46px;
    display: flex;
    align-items: center;
    gap: 12px;
    font-family: "Cinzel", "Times New Roman", serif;
    font-weight: 400;
    font-size: 27px;
    color: var(--brand-blue);
  }
  .brand-name .brand-square {
    width: 14px;
    height: 14px;
    background: var(--brand-blue);
  }
  .content-column {
    position: absolute;
    top: 226px;
    width: 440px;
  }
  .content-column.left { left: 105px; }
  .content-column.right { left: 662px; top: 223px; }
  .column-heading {
    font-family: "Cinzel", "Times New Roman", serif;
    font-weight: 400;
    font-size: 28px;
    color: var(--brand-blue);
    margin-bottom: 18px;
    white-space: nowrap;
  }
  .column-text {
    font-size: 17.5px;
    line-height: 33px;
    color: var(--body-text);
    text-align: justify;
    margin-bottom: 33px;
  }
  .slide-footer {
    position: absolute;
    left: 0; bottom: 0;
    width: 100%;
    height: 56px;
    background: var(--footer-blue);
    border-top: 4px solid var(--footer-rule);
    color: var(--white);
    font-size: 19px;
  }
  .copyright {
    position: absolute;
    left: 19px;
    top: 11px;
  }
  .page-number {
    position: absolute;
    right: 17px;
    top: 11px;
    font-weight: 700;
  }
</style>
</head>
<body>
  <div class="slide">
    <header class="slide-header">
      <h1 class="project-title"><span class="accent">Project</span> Title Here</h1>
      <div class="brand-name"><span class="brand-square"></span>The Harbinger Collective</div>
    </header>

    <section class="content-column left">
      <h2 class="column-heading">Lorem ipsum dolor sit ipsum</h2>
      <p class="column-text">Lorem ipsum dolor sit ipsum Lorem ipsum dolor sit ipsum Lorem ipsum dolor sit ipsum Lorem ipsum dolor sit ipsum lorem ipsum dolor sit ipsum Lorem ipsum dolor sit ipsum Lorem ipsum dolor sit ipsum</p>
      <p class="column-text">Lorem ipsum dolor sit ipsum Lorem ipsum dolor sit ipsum Lorem ipsum dolor sit ipsum Lorem ipsum dolor sit ipsum lorem ipsum dolor sit ipsum Lorem ipsum dolor sit ipsum Lorem ipsum dolor sit ipsum Lorem ipsum dolor sit ipsum</p>
    </section>

    <section class="content-column right">
      <h2 class="column-heading">Lorem ipsum dolor sit ipsum</h2>
      <p class="column-text">Lorem ipsum dolor sit ipsum Lorem ipsum dolor sit ipsum Lorem ipsum dolor sit ipsum Lorem ipsum dolor sit ipsum lorem ipsum dolor sit ipsum Lorem ipsum dolor sit ipsum Lorem ipsum dolor sit ipsum</p>
      <p class="column-text">Lorem ipsum dolor sit ipsum Lorem ipsum dolor sit ipsum Lorem ipsum dolor sit ipsum Lorem ipsum dolor sit ipsum lorem ipsum dolor sit ipsum Lorem ipsum dolor sit ipsum Lorem ipsum dolor sit ipsum Lorem ipsum dolor sit ipsum</p>
    </section>

    <footer class="slide-footer">
      <span class="copyright">Copyright text here</span>
      <span class="page-number">Page : 01</span>
    </footer>
  </div>
</body>
</html>
```